Wine label design for my wife. Wine called "The Mirabel"

I need a wine label face lift of one of my premium wines in my collection. My wine sells in Harbor Lark's all over the States. My current label is called The Mirabel (my wife's name) and the illustration of her eyes is done by a well know artist from South Africa. I do not have to use this illustration and therefor I attached several pictures of her and her eyes, even when she was a little girl. The wine's also made in South Africa. This is a premium wine that we only sell 2000 bottles per year. The wine sells at 60 usd per bottle, The current label is too white. I also think her eyes should look more at the person buying it, than away from them.

Target Market(s)

Top end wine buyers

Font styles to use
Decorative
Script

Requirements
Must have
• 'The Mirabel' must be on the label
An illustration must be on the label
Basically all the info that's on the current label must be on by law. As per Sample
Nice to have
• Maybe some ideas of her whole face?
Should not have
• any gold colour

```html
<!DOCTYPE html>
<html lang="en">
<head>
<meta charset="utf-8">
<title>The Mirabel – Grand Reserve Label</title>
<link rel="stylesheet" href="https://fonts.googleapis.com/css2?family=Libre+Baskerville:wght@400;700&family=Cormorant+Garamond:wght@400;500&family=Pinyon+Script&display=swap">
<style>
  :root {
    --backdrop-top: #e6eaef;
    --backdrop-bottom: #d9dfe7;
    --label-paper: #f3efe2;
    --label-paper-edge: #ebe5d3;
    --frame-line: #b9b4a5;
    --frame-line-soft: #d3cebf;
    --ink: #6d6a61;
    --ink-dark: #57544c;
    --accent-red: #8c1d1d;
    --portrait-light: #e4e4e4;
    --portrait-dark: #8f8f8f;
    --ornament: #c9c4b6;
  }
  * { margin: 0; padding: 0; box-sizing: border-box; }
  html, body {
    width: 740px;
    height: 1200px;
    overflow: hidden;
  }
  body {
    background: linear-gradient(180deg, var(--backdrop-top), var(--backdrop-bottom));
  }
  .label-canvas { display: block; width: 740px; height: 1200px; }
  .label-shape { fill: url(#paperTone); }
  .frame-outer { fill: none; stroke: var(--frame-line); stroke-width: 2; }
  .frame-inner { fill: none; stroke: var(--frame-line-soft); stroke-width: 1.5; }
  .heading-arc {
    font-family: "Libre Baskerville", serif;
    font-weight: 700;
    font-size: 27px;
    letter-spacing: 1px;
    fill: var(--ink-dark);
  }
  .accent-dot { fill: var(--accent-red); }
  .portrait-ring { fill: none; stroke: var(--frame-line-soft); stroke-width: 2; }
  .ornament-area { fill: var(--ornament); opacity: 0.55; }
  .wine-name {
    font-family: "Pinyon Script", cursive;
    font-size: 92px;
    fill: var(--ink);
  }
  .rule { stroke: var(--frame-line-soft); stroke-width: 1.5; }
  .varietal {
    font-family: "Cormorant Garamond", serif;
    font-weight: 500;
    font-size: 33px;
    letter-spacing: 1px;
    fill: var(--ink);
  }
  .producer {
    font-family: "Libre Baskerville", serif;
    font-weight: 700;
    font-size: 16px;
    letter-spacing: 0.5px;
    fill: var(--ink);
  }
  .rule-accent { stroke: var(--accent-red); stroke-width: 2; }
</style>
</head>
<body>
<svg class="label-canvas" viewBox="0 0 740 1200" xmlns="http://www.w3.org/2000/svg">
  <defs>
    <linearGradient id="paperTone" x1="0" y1="0" x2="0" y2="1">
      <stop offset="0" stop-color="var(--label-paper)"/>
      <stop offset="1" stop-color="var(--label-paper-edge)"/>
    </linearGradient>
    <radialGradient id="portraitTone" cx="0.5" cy="0.5" r="0.6">
      <stop offset="0" stop-color="var(--portrait-light)"/>
      <stop offset="1" stop-color="var(--portrait-dark)"/>
    </radialGradient>
    <path id="labelOutline" d="M40,60 C150,60 170,0 310,0 C450,0 470,60 580,60 A40,40 0 0 0 620,100 L620,715 A40,40 0 0 0 580,755 L40,755 A40,40 0 0 0 0,715 L0,100 A40,40 0 0 0 40,60 Z"/>
    <path id="headingCurve" d="M140,148 Q310,70 480,148"/>
  </defs>

  <g class="wine-label" transform="translate(60,222)">
    <use href="#labelOutline" class="label-shape"/>
    <use href="#labelOutline" class="frame-outer" transform="translate(12,12) scale(0.9613,0.9682)"/>
    <use href="#labelOutline" class="frame-inner" transform="translate(20,20) scale(0.9355,0.947)"/>

    <text class="heading-arc" text-anchor="middle">
      <textPath href="#headingCurve" startOffset="50%">GRAND RESERVE</textPath>
    </text>
    <circle class="accent-dot" cx="310" cy="131" r="5"/>

    <ellipse class="portrait-ring" cx="310" cy="240" rx="172" ry="108"/>
    <ellipse cx="310" cy="240" rx="160" ry="97" fill="url(#portraitTone)" role="img" aria-label="Black-and-white portrait illustration of Mirabel's eyes"/>

    <rect class="ornament-area" x="38" y="236" width="118" height="24" rx="12" role="img" aria-label="Decorative scroll flourish"/>
    <rect class="ornament-area" x="464" y="236" width="118" height="24" rx="12" role="img" aria-label="Decorative scroll flourish"/>

    <text class="wine-name" x="310" y="478" text-anchor="middle">The Mirabel</text>

    <line class="rule" x1="48" y1="516" x2="572" y2="516"/>
    <text class="varietal" x="310" y="584" text-anchor="middle">SAUVIGNON BLANC 2017</text>
    <line class="rule" x1="48" y1="622" x2="572" y2="622"/>

    <line class="rule-accent" x1="81" y1="696" x2="183" y2="696"/>
    <text class="producer" x="310" y="701" text-anchor="middle">ELIAS MARSH WINES</text>
    <line class="rule-accent" x1="437" y1="696" x2="539" y2="696"/>
  </g>
</svg>
</body>
</html>
```